Photography Catalog/Portfolio for a Photographer's Studio

I would like to have a photography portfolio/catalog designed for distribution to potential high end clients as a hard copy and soft copy to send via email. The total number of pages will be about 35-50. I will provide the photos. I would like the catalog to be 8X10 size in portrait mode. I am open to creative ideas. My work can be viewed at www.studiovelmora.com. The catalog/portfolio will be divided into Architecture Photography, Fine Art and Corporate Portraits. It will talk a bit about my work philosophy, my creative process.
I have provided a sample of the type of catalog I am looking for. I will provide the text as necessary.

Target Market(s)

Potential clients for Architecture Photography, Fine Art and Corporate Portraits/Lifestyle.

Industry/Entity Type

Architecture

Colors

Designer to choose colors to be used in the design.

Requirements
Must have
• At least 10 images in each section, a narrative as required. Most of fine art will be black and white images, Architecture will be in color and Portraits will be a combination of B/W and Color.

```html
<!DOCTYPE html>
<html lang="en">
<head>
<meta charset="utf-8">
<title>Velmora Photographic Prize — Catalog Cover</title>
<link rel="stylesheet" href="https://fonts.googleapis.com/css2?family=Tinos:wght@400;700&family=Arimo:wght@700&display=swap">
<style>
  :root {
    --backdrop: #6f6f6f;
    --cover-black: #0d0d0d;
    --cover-white: #fafafa;
    --rule-light: #cfcfcf;
    --rule-dark: #1a1a1a;
    --ink: #111111;
    --photo-light: #c9c9c9;
    --photo-mid: #7c7c7c;
    --photo-dark: #3a3a3a;
    --photo-deep: #262626;
  }
  * { margin: 0; padding: 0; box-sizing: border-box; }
  html, body {
    width: 1200px;
    height: 824px;
    overflow: hidden;
    background: var(--backdrop);
  }
  .spread {
    position: absolute;
    left: 60px;
    top: 52px;
    width: 1080px;
    height: 720px;
    display: flex;
    box-shadow: 0 12px 32px rgba(0,0,0,0.4);
  }
  .page {
    position: relative;
    width: 540px;
    height: 720px;
  }
  .back-cover {
    background: var(--cover-black);
  }
  .back-cover .frame {
    position: absolute;
    inset: 16px;
    border: 1px solid var(--rule-light);
  }
  .front-cover {
    background: var(--cover-white);
    box-shadow: inset 6px 0 10px -6px rgba(0,0,0,0.25);
  }
  .front-cover .frame {
    position: absolute;
    inset: 14px;
    border: 1px solid var(--rule-dark);
  }
  .brand {
    position: absolute;
    top: 40px;
    left: 0;
    right: 0;
    display: flex;
    flex-direction: column;
    align-items: center;
  }
  .brand-dot {
    width: 66px;
    height: 66px;
    border-radius: 50%;
    background: var(--cover-black);
  }
  .brand-name {
    margin-top: 7px;
    font-family: "Tinos", "Times New Roman", serif;
    font-weight: 400;
    font-size: 13px;
    letter-spacing: 4px;
    color: var(--ink);
  }
  .cover-photo {
    position: absolute;
    top: 168px;
    left: 48px;
    width: 444px;
    height: 300px;
    background:
      linear-gradient(180deg, var(--photo-light) 0%, var(--photo-mid) 14%, transparent 30%),
      linear-gradient(165deg, var(--photo-dark) 0%, var(--photo-dark) 42%, var(--photo-light) 58%, var(--photo-mid) 70%, var(--photo-deep) 100%);
  }
  .cover-title {
    position: absolute;
    top: 488px;
    left: 0;
    right: 0;
    text-align: center;
    font-family: "Tinos", "Times New Roman", serif;
    color: var(--ink);
    font-size: 24px;
    line-height: 1.12;
  }
  .cover-title .title-name { font-weight: 700; display: block; }
  .cover-title .title-line { font-weight: 400; display: block; }
  .copyright {
    position: absolute;
    top: 592px;
    left: 0;
    right: 0;
    text-align: center;
    font-family: "Arimo", Arial, sans-serif;
    font-weight: 700;
    font-size: 8px;
    color: var(--ink);
  }
</style>
</head>
<body>
  <main class="spread">
    <section class="page back-cover">
      <div class="frame"></div>
    </section>
    <section class="page front-cover">
      <div class="frame"></div>
      <header class="brand">
        <div class="brand-dot"></div>
        <div class="brand-name">VELMORA</div>
      </header>
      <div class="cover-photo" role="img" aria-label="Black and white architectural photograph of grey concrete blocks casting deep shadows"></div>
      <h1 class="cover-title">
        <span class="title-name">Velmora</span>
        <span class="title-line">Photographic</span>
        <span class="title-line">Prize</span>
      </h1>
      <p class="copyright">© Velmora and Grayline LLC all rights reserved</p>
    </section>
  </main>
</body>
</html>
```